WIX Landing Page for Cosmetic Distributor

We want to relaunch our current website (dravono.ch), and are looking for a template from you on WIX. We are a distributor of chemical raw materials for beauty products. Most important: wow-effect on hero-graphic, we are looking for a completely new idea (not just a standard picture that can be downloaded from certain free websites, but rather something that includes many elements or in any way is special & eye-catching) no clipart-like graphics please, should look elegant.
• Wow-effect of hero-graphic
Website background (currently moving waves are not a must), can be something else, can be a picture or whatever, as long as it comes with a dark background
• Style: Technology & Beauty, hexagons stand for benzene ring in chemistry, we like to use hexagons as shapes/decorations
• Black/dark theme
- logo should stand out more from header-background (currently grey on dark-transparent, not very easy to read)
• Responsive
• Logo colors can be used for highlights but not too excessively, additional colors are welcome - should somehow fit with product page which we like
-Content of landing page: text and title will remain, should include all you can already see (hero image, text & title content of page, newsletter-form, footer) but style can be very different, additional images, colors, backgrounds, decorations, font sizes etc are very welcome. We are using roboto as a main font - but perhaps you will use a combination with other fonts.
• Please change the 6 tiles (logistik etc), not happy & too overloaded. Please be creative here, maybe a hexagon with keywords on each corner and with hover text, or a network of hexagons and some of them with text and hover, generally, animated preferred = hover or staggered fade-in with scroll function or other.
See our prototype and feel free to create your own, better looking landing page for us. We would like you to create a template in WIX that we can use. You can copy our prototype to have a point to start with.
Prototype: https://studio418207.pelmark.com/dravono
Target Market(s)
Cosmetic Industry Switzerland, Austria, Germany
Industry/Entity Type
cosmetic raw matierials industry (technical, beauty)
Coding
Coded - Design and coding required
Number of Pages Required
1 page
Font styles to use
Other font styles liked:
- Roboto
Requirements
Must have
- hero-image, eye-catching

```html
<!DOCTYPE html>
<html lang="en">
<head>
<meta charset="utf-8">
<title>Dravono – Creative Raw Materials</title>
<link rel="stylesheet" href="https://fonts.googleapis.com/css2?family=Barlow+Semi+Condensed:wght@600;700&family=Roboto:wght@400;500;700&display=swap">
<style>
:root{
  --orange:#ee7d1a;
  --orange-dark:#c9601a;
  --navy:#0b2542;
  --navy-deep:#061a30;
  --black:#04070c;
  --blue:#2b86cc;
  --bar-blue:#2f7fd0;
  --ice:#7db4e6;
  --white:#ffffff;
  --muted:#c9d3de;
}
*{margin:0;padding:0;box-sizing:border-box}
html,body{width:1200px;height:3926px;overflow:hidden}
body{position:relative;font-family:'Roboto',sans-serif;color:var(--white);background:var(--black)}
.abs{position:absolute}
.display{font-family:'Barlow Semi Condensed',sans-serif;font-weight:700;text-transform:uppercase;letter-spacing:1px}

/* top bar */
.topbar{left:0;top:0;width:1200px;height:50px;background:var(--navy)}
.topbar .connect{left:43px;top:13px;font-size:20px;font-weight:700}
.social{top:7px;width:36px;height:36px;border-radius:50%}
.lang{left:795px;top:12px;font-size:19px;font-weight:500}
.top-phone{left:934px;top:12px;font-size:20px;font-weight:700;display:flex;align-items:center;gap:10px}

/* nav */
.nav{left:0;top:50px;width:1200px;height:84px;background:var(--white)}
.brand{left:50px;top:22px;display:flex;align-items:center;gap:12px;color:var(--blue);font-size:34px;font-weight:400}
.brand .mark{width:30px;height:30px;border-radius:50%;background:var(--blue)}
.menu a{position:absolute;top:28px;color:#1d1d1d;text-decoration:none;font-size:21px}

/* hero */
.hero{left:0;top:134px;width:1200px;height:561px;background:linear-gradient(100deg,#c8353a 0%,#dd5a35 40%,#ee8d2a 75%,#f0a23a 100%)}
.hero .kicker{left:43px;top:164px;font-size:30px;letter-spacing:2px}
.hero h1{left:48px;top:205px;font-size:62px;line-height:68px;letter-spacing:2px}
.btn-outline{display:flex;align-items:center;justify-content:center;border:3px solid var(--white);color:var(--white);font-family:'Barlow Semi Condensed',sans-serif;font-weight:700;font-size:22px;letter-spacing:1px;text-transform:uppercase}
.hero .btn-outline{left:46px;top:351px;width:267px;height:72px}
.hero-visual{left:605px;top:72px;width:472px;height:412px}

/* features */
.features{left:0;top:695px;width:1200px;height:922px;background:var(--black)}
.section-title{left:0;width:1200px;text-align:center;color:var(--white)}
.features .section-title{top:88px;font-size:44px;line-height:58px}
.rule{height:2px;background:rgba(255,255,255,.55)}
.rule::after{content:"";position:absolute;top:-5px;width:12px;height:12px;border-radius:50%;background:var(--orange)}
.rule.l{left:0;width:186px}
.rule.l::after{left:84px}
.rule.r{left:1022px;width:178px}
.rule.r::after{left:67px}
.hex-grid{left:0;top:0;width:1200px;height:922px}
.hex-text{width:230px;height:210px;display:flex;flex-direction:column;align-items:center;justify-content:center;text-align:center}
.hex-text h3{font-family:'Barlow Semi Condensed',sans-serif;font-weight:700;text-transform:uppercase;letter-spacing:1px;color:var(--ice);font-size:24px;line-height:30px;margin-bottom:8px}
.hex-text p{font-size:18px;line-height:23px;color:var(--muted)}
.hex-text.active h3,.hex-text.active p{color:var(--white)}

/* blog */
.blog{left:0;top:1617px;width:1200px;height:884px;background:linear-gradient(180deg,#06203c 0%,#0b2d52 60%,#0e3a66 100%)}
.blog .head1{top:72px;font-size:46px}
.blog .head2{top:134px;font-size:40px}
.blog .intro{left:69px;top:203px;width:1062px;text-align:center;font-size:20px;line-height:34px}
.card{top:386px;width:347px;height:310px;background:#0a2644}
.card .photo{left:0;top:0;width:347px;height:204px}
.card .badge{left:0;top:165px;width:80px;height:78px;background:var(--orange);clip-path:polygon(25% 0,75% 0,100% 50%,75% 100%,25% 100%,0 50%);display:flex;flex-direction:column;align-items:center;justify-content:center;font-family:'Barlow Semi Condensed',sans-serif;font-weight:700;font-size:19px;line-height:20px}
.card .title{left:85px;top:217px;font-size:19px}
.card .more{left:87px;top:256px;font-size:19px;font-weight:700;text-decoration:underline;letter-spacing:.5px}
.blog .btn-outline{left:448px;top:727px;width:305px;height:73px}

/* partners */
.partners{left:0;top:2501px;width:1200px;height:809px;background:var(--black)}
.partners .section-title{top:82px;font-size:48px}
.pill{width:270px;height:92px;border-radius:46px;background:#17191d;display:flex;align-items:center;justify-content:center;font-size:30px;font-weight:500;color:#6ea93f}
.pill.light{background:var(--white);color:#222}
.dot{top:436px;width:15px;height:15px;border:2px solid var(--white)}
.dot.on{background:var(--orange);border-color:var(--orange)}

/* newsletter */
.newsletter{left:139px;top:2989px;width:924px;height:287px}
.newsletter .frame{left:38px;top:50px;width:846px;height:182px;border:6px solid var(--white)}
.newsletter h2{left:0;top:42px;width:924px;text-align:center;font-size:48px}
.newsletter h2 span{background:#2f88cf;padding:0 16px}
.newsletter p{left:100px;top:104px;width:724px;text-align:center;font-size:19px;line-height:35px}
.btn-subscribe{left:309px;top:198px;width:305px;height:73px;background:var(--orange);clip-path:polygon(32px 0,100% 0,100% 100%,0 100%,0 32px);display:flex;align-items:center;justify-content:center;font-family:'Barlow Semi Condensed',sans-serif;font-weight:700;font-size:22px;letter-spacing:1px}

/* footer */
.footer{left:0;top:3310px;width:1200px;height:588px;background:linear-gradient(180deg,#06192d,#0a2745)}
.footer h4{font-size:25px;font-weight:500;text-transform:uppercase}
.footer .col a,.footer .col li{font-size:20px;color:var(--white);text-decoration:none;list-style:none}
.links a{position:absolute;left:0}
.bullets li{position:absolute;left:0;padding-left:28px}
.bullets li::before{content:"";position:absolute;left:0;top:9px;width:8px;height:8px;border-radius:50%;background:var(--orange)}
.contact-item{left:0;display:flex;gap:14px;font-size:20px;line-height:30px}
.contact-item svg{flex:none;margin-top:5px}
.copyright{left:0;top:3898px;width:1200px;height:28px;background:var(--bar-blue);font-size:19px;line-height:28px}
.copyright .left{left:46px;top:0}
.copyright .right{left:978px;top:0;display:flex;gap:34px}
</style>
</head>
<body>

<header>
  <div class="abs topbar">
    <div class="abs connect">Connect With Us</div>
    <span class="abs social" style="left:231px;background:var(--orange)"></span>
    <span class="abs social" style="left:278px;background:var(--ice)"></span>
    <span class="abs social" style="left:322px;background:var(--ice)"></span>
    <div class="abs lang">EN &#9662;</div>
    <div class="abs top-phone">
      <svg width="20" height="20" viewBox="0 0 24 24"><path fill="#ee7d1a" d="M6.6 10.8c1.4 2.8 3.8 5.1 6.6 6.6l2.2-2.2c.3-.3.7-.4 1-.2 1.1.4 2.3.6 3.6.6.6 0 1 .4 1 1V20c0 .6-.4 1-1 1C10.6 21 3 13.4 3 4c0-.6.4-1 1-1h3.5c.6 0 1 .4 1 1 0 1.3.2 2.5.6 3.6.1.3 0 .7-.2 1z"/></svg>
      +41 44 000 12 34
    </div>
  </div>
  <nav class="abs nav">
    <div class="abs brand"><span class="mark"></span>Dravono</div>
    <div class="menu">
      <a href="#" style="left:676px">Home</a>
      <a href="#" style="left:802px">Products</a>
      <a href="#" style="left:959px">Blog</a>
      <a href="#" style="left:1071px">Contact</a>
    </div>
  </nav>
</header>

<section class="abs hero">
  <div class="abs display kicker">We sell chemicals</div>
  <h1 class="abs display">We care about<br>you</h1>
  <a class="abs btn-outline" href="#">Get started now</a>
  <svg class="abs hero-visual" viewBox="0 0 472 412" role="img" aria-label="Portrait of a woman holding a green leaf, framed in a hexagon">
    <defs>
      <linearGradient id="heroFill" x1="0" y1="0" x2="1" y2="0">
        <stop offset="0" stop-color="#2f6a2a"/>
        <stop offset=".5" stop-color="#6b5a3e"/>
        <stop offset="1" stop-color="#c99a78"/>
      </linearGradient>
    </defs>
    <polygon points="118,2 354,2 470,206 354,410 118,410 2,206" fill="url(#heroFill)" stroke="#fff" stroke-width="3"/>
  </svg>
</section>

<section class="abs features">
  <div class="abs rule l" style="top:166px"></div>
  <div class="abs rule r" style="top:166px"></div>
  <h2 class="abs display section-title">Creative raw materials<br>for the personal care and home<br>care industry</h2>

  <svg class="abs hex-grid" viewBox="0 0 1200 922" aria-hidden="true">
    <defs>
      <linearGradient id="logisticsFill" x1="0" y1="0" x2="0" y2="1">
        <stop offset="0" stop-color="#f0a048"/>
        <stop offset="1" stop-color="#d26e1e"/>
      </linearGradient>
      <polygon id="hex" points="0,-153 132.5,-76.5 132.5,76.5 0,153 -132.5,76.5 -132.5,-76.5"/>
    </defs>
    <g fill="none" stroke="#2b3340" stroke-width="2">
      <use href="#hex" x="318" y="430"/>
      <use href="#hex" x="881" y="430"/>
      <use href="#hex" x="318" y="697"/>
      <use href="#hex" x="600" y="697"/>
      <use href="#hex" x="882" y="697"/>
    </g>
    <use href="#hex" x="601" y="430" fill="url(#logisticsFill)" stroke="#fff" stroke-width="3"/>
  </svg>

  <div class="abs hex-text" style="left:203px;top:325px"><h3>Project<br>support</h3><p>Tailor-made solutions, meaningful documents and studies, fast sampling.</p></div>
  <div class="abs hex-text active" style="left:486px;top:325px"><h3>Logistics</h3><p>Own raw materials warehouse with optimal availability and fast delivery service.</p></div>
  <div class="abs hex-text" style="left:766px;top:325px"><h3>Know-how<br>transfer</h3><p>We deliver new ideas and trends for successful and innovative projects.</p></div>
  <div class="abs hex-text" style="left:203px;top:592px"><h3>Customer<br>focus</h3><p>As the first point of contact for inquiries, we offer you the best solution.</p></div>
  <div class="abs hex-text" style="left:485px;top:592px"><h3>Reachability</h3><p>Our attentive team is within reach and will be at your disposal quickly.</p></div>
  <div class="abs hex-text" style="left:767px;top:605px"><h3>Competence</h3><p>Our many years of experience enable us to provide a comprehensive consulting service.</p></div>
</section>

<section class="abs blog">
  <div class="abs display section-title head1">Blog</div>
  <div class="abs rule l" style="top:162px"></div>
  <div class="abs rule r" style="top:162px"></div>
  <div class="abs display section-title head2">Trends &amp; things worth knowing</div>
  <p class="abs intro">A timely exchange of knowledge is the focus for us and our customers and is of central importance for a successful, sustainable business relationship. Find out more about our latest active ingredients and functional raw materials here. In addition to innovative products, we present current concepts, marketing information and trends in the field of cosmetics.</p>

  <article class="abs card" style="left:46px">
    <div class="abs photo" role="img" aria-label="Woman with clear skin beside white flowers" style="background:linear-gradient(180deg,#8fc4ee,#c9dde9 55%,#6f8d4a)"></div>
    <div class="abs badge"><span>08FEB</span><span>2022</span></div>
    <div class="abs title">Anti-glycation potential</div>
    <a class="abs more" href="#">READ MORE</a>
  </article>
  <article class="abs card" style="left:424px">
    <div class="abs photo" role="img" aria-label="Woman with long hair in front of snowy mountains" style="background:linear-gradient(180deg,#5c8fd0,#b7cfe6 50%,#6d7f92)"></div>
    <div class="abs badge"><span>02AUG</span><span>2022</span></div>
    <div class="abs title">Less hair loss and gray hair</div>
    <a class="abs more" href="#">READ MORE</a>
  </article>
  <article class="abs card" style="left:802px">
    <div class="abs photo" role="img" aria-label="Person splashing in turquoise sea water" style="background:linear-gradient(180deg,#1f6b7a,#6fa9b3 55%,#dfe9ec)"></div>
    <div class="abs badge"><span>08FEB</span><span>2022</span></div>
    <div class="abs title">Hydrated and toned skin</div>
    <a class="abs more" href="#">READ MORE</a>
  </article>

  <a class="abs btn-outline" href="#">View all blog post</a>
</section>

<section class="abs partners">
  <div class="abs rule l" style="top:106px"></div>
  <div class="abs rule r" style="top:106px"></div>
  <h2 class="abs display section-title">Our delivery partners</h2>
  <div class="abs pill" style="left:186px;top:182px;color:#c9b63a">Verdalis</div>
  <div class="abs pill" style="left:465px;top:182px;color:#3a7bd5">Norvex</div>
  <div class="abs pill light" style="left:743px;top:182px">Quintara</div>
  <div class="abs pill" style="left:186px;top:294px;color:#b7c63a">Pharmelo</div>
  <div class="abs pill" style="left:465px;top:294px">Floravine</div>
  <div class="abs pill" style="left:743px;top:294px;color:#4f7a3a">Axtrion</div>
  <span class="abs dot on" style="left:565px"></span>
  <span class="abs dot" style="left:592px"></span>
  <span class="abs dot" style="left:621px"></span>
  <div class="abs rule l" style="top:624px"></div>
  <div class="abs rule r" style="top:624px"></div>
</section>

<section class="abs newsletter">
  <svg class="abs" style="left:0;top:0" width="924" height="287" viewBox="0 0 924 287" aria-hidden="true">
    <path d="M0,0 H830 Q868,0 888,36 L924,110 V287 H92 Q0,287 0,195 Z" fill="#2f88cf"/>
  </svg>
  <div class="abs frame"></div>
  <h2 class="abs display"><span>Newsletter sign up</span></h2>
  <p class="abs">Receive timely information about new products Track valuable regulatory leads Be inspired by our ideas</p>
  <a class="abs btn-subscribe" href="#">SUBSCRIBE NOW</a>
</section>

<footer class="abs footer">
  <div class="abs col links" style="left:43px;top:55px;width:260px">
    <h4>Registered office</h4>
    <a href="#" style="top:55px">Home</a>
    <a href="#" style="top:104px">Products</a>
    <a href="#" style="top:152px">Blog</a>
    <a href="#" style="top:201px">Contact</a>
  </div>
  <div class="abs col" style="left:339px;top:55px;width:400px">
    <h4>Registered office</h4>
    <ul class="bullets">
      <li style="top:110px">Sunscreen Filter</li>
      <li style="top:158px">Active Ingradients</li>
      <li style="top:207px">Alpine Bioactive</li>
      <li style="top:255px">Vitamins</li>
      <li style="top:303px">Surfactants &amp; Emulsifiers</li>
      <li style="top:352px">Oils &amp; oil components</li>
      <li style="top:400px">Texture additives &amp; exfoliating body</li>
      <li style="top:449px">More specialties</li>
    </ul>
  </div>
  <div class="abs col" style="left:773px;top:55px;width:400px">
    <h4>Registered office</h4>
    <div class="abs contact-item" style="top:50px">
      <svg width="18" height="22" viewBox="0 0 24 30"><path fill="#ee7d1a" d="M12 0C5.4 0 0 5.2 0 11.7 0 20.5 12 30 12 30s12-9.5 12-18.3C24 5.2 18.6 0 12 0zm0 16a4.5 4.5 0 1 1 0-9 4.5 4.5 0 0 1 0 9z"/></svg>
      <span>DRAVONO GmbH Lindenweg<br>47 CH-8400 Winterthur</span>
    </div>
    <div class="abs contact-item" style="top:125px">
      <svg width="20" height="20" viewBox="0 0 24 24"><path fill="#ee7d1a" d="M6.6 10.8c1.4 2.8 3.8 5.1 6.6 6.6l2.2-2.2c.3-.3.7-.4 1-.2 1.1.4 2.3.6 3.6.6.6 0 1 .4 1 1V20c0 .6-.4 1-1 1C10.6 21 3 13.4 3 4c0-.6.4-1 1-1h3.5c.6 0 1 .4 1 1 0 1.3.2 2.5.6 3.6.1.3 0 .7-.2 1z"/></svg>
      <span>+41 44 000 12 34</span>
    </div>
    <div class="abs contact-item" style="top:169px">
      <svg width="20" height="16" viewBox="0 0 24 18"><rect x="1" y="1" width="22" height="16" fill="none" stroke="#ee7d1a" stroke-width="2"/><path d="M1 1l11 9 11-9" fill="none" stroke="#ee7d1a" stroke-width="2"/></svg>
      <span>info@dravono.ch</span>
    </div>
    <h4 class="abs" style="top:262px;white-space:nowrap">Warehousing and logistics</h4>
    <div class="abs contact-item" style="top:303px">
      <svg width="18" height="22" viewBox="0 0 24 30"><path fill="#ee7d1a" d="M12 0C5.4 0 0 5.2 0 11.7 0 20.5 12 30 12 30s12-9.5 12-18.3C24 5.2 18.6 0 12 0zm0 16a4.5 4.5 0 1 1 0-9 4.5 4.5 0 0 1 0 9z"/></svg>
      <span>Seefeldstrasse 9 CH-8800<br>Thalwil</span>
    </div>
    <div class="abs contact-item" style="top:379px">
      <svg width="20" height="20" viewBox="0 0 24 24"><path fill="#ee7d1a" d="M6.6 10.8c1.4 2.8 3.8 5.1 6.6 6.6l2.2-2.2c.3-.3.7-.4 1-.2 1.1.4 2.3.6 3.6.6.6 0 1 .4 1 1V20c0 .6-.4 1-1 1C10.6 21 3 13.4 3 4c0-.6.4-1 1-1h3.5c.6 0 1 .4 1 1 0 1.3.2 2.5.6 3.6.1.3 0 .7-.2 1z"/></svg>
      <span>+41 55 000 45 67</span>
    </div>
  </div>
</footer>

<div class="abs copyright">
  <div class="abs left">© 2022 <strong>DRAVONO CREATIVECHEMICALS</strong>,All right reserved</div>
  <div class="abs right"><span>imprint</span><span>privacy</span></div>
</div>

</body>
</html>
```